Corvane Building Materials letterhead template

Simple but professional letterhead template for business communication.
LOGO/name in upper left, balanced by company contact info on right upper.
Subject description, date...
addressee, cc: and BC: if applicable editable info..

Need extra days to review

```html
<!DOCTYPE html>
<html lang="en">
<head>
<meta charset="utf-8">
<title>Corvane Building Materials — Letterhead</title>
<link rel="stylesheet" href="https://fonts.googleapis.com/css2?family=Archivo:wght@800&family=Poppins:wght@400;600&family=Open+Sans:wght@400&display=swap">
<style>
  :root {
    --brand-blue: #2a5eab;
    --watermark-tint: #e0e3f1;
    --ink: #1a1a1a;
    --paper: #ffffff;
    --backdrop: #d4d9d9;
  }
  * { margin: 0; padding: 0; box-sizing: border-box; }
  html, body {
    width: 1200px;
    height: 1028px;
    overflow: hidden;
    background: var(--backdrop);
  }
  .letterhead {
    position: absolute;
    left: 257px;
    top: 30px;
    width: 686px;
    height: 968px;
    background: var(--paper);
    overflow: hidden;
  }
  .brand {
    position: absolute;
    left: 36px;
    top: 36px;
    display: flex;
    align-items: center;
    gap: 13px;
  }
  .brand-square {
    width: 98px;
    height: 98px;
    background: var(--brand-blue);
  }
  .brand-name {
    font-family: "Archivo", sans-serif;
    font-weight: 800;
    font-size: 28px;
    line-height: 33px;
    letter-spacing: 1.2px;
    color: var(--brand-blue);
    text-transform: uppercase;
  }
  .contact {
    position: absolute;
    right: 36px;
    top: 33px;
    font-family: "Poppins", sans-serif;
    font-size: 14px;
    color: var(--ink);
    list-style: none;
  }
  .contact-item {
    display: flex;
    justify-content: flex-end;
    align-items: flex-start;
    gap: 8px;
    line-height: 18.5px;
  }
  .contact-item.address { margin-bottom: 13px; }
  .contact-icon {
    width: 14px;
    height: 16px;
    flex: none;
    margin-top: 1px;
    fill: var(--brand-blue);
  }
  .contact-text { text-align: right; letter-spacing: 0.4px; }
  .letter-meta {
    position: absolute;
    left: 38px;
    top: 183px;
  }
  .meta-date {
    font-family: "Open Sans", sans-serif;
    font-size: 13px;
    color: var(--ink);
  }
  .meta-subject {
    margin-top: 6px;
    font-family: "Poppins", sans-serif;
    font-weight: 600;
    font-size: 14px;
    color: var(--brand-blue);
  }
  .watermark-block {
    position: absolute;
    left: 102px;
    top: 365px;
    width: 449px;
    height: 402px;
    background: var(--watermark-tint);
  }
  .footer-band {
    position: absolute;
    left: 0;
    bottom: 0;
    width: 686px;
    height: 15px;
  }
  .footer-band polygon { fill: var(--brand-blue); }
</style>
</head>
<body>
  <main class="letterhead">
    <header>
      <div class="brand">
        <div class="brand-square"></div>
        <div class="brand-name">Corvane<br>Building<br>Materials</div>
      </div>

      <ul class="contact">
        <li class="contact-item address">
          <span class="contact-text">47 Harlow Crest Ave.<br>Linden Bay, CA 93024</span>
          <svg class="contact-icon" viewBox="0 0 14 16" aria-hidden="true"><path d="M7 0a5 5 0 0 0-5 5c0 3.6 5 8.5 5 8.5S12 8.6 12 5a5 5 0 0 0-5-5zm0 7.2A2.2 2.2 0 1 1 7 2.8a2.2 2.2 0 0 1 0 4.4z"/><ellipse cx="7" cy="14.6" rx="4.5" ry="1.2" fill="none" stroke="#2a5eab" stroke-width="1"/></svg>
        </li>
        <li class="contact-item">
          <span class="contact-text">1-805-555-0148</span>
          <svg class="contact-icon" viewBox="0 0 14 16" aria-hidden="true"><path d="M3.2 2.5l2 2.6-1.2 1.3c.8 1.8 2.2 3.2 4 4l1.3-1.2 2.6 2-1.3 2C6.2 13 1.9 8.7 1.2 4z"/><path d="M8 2.5a4 4 0 0 1 4 4M8 4.6a2 2 0 0 1 2 2" fill="none" stroke="#2a5eab" stroke-width="1.2"/></svg>
        </li>
        <li class="contact-item">
          <span class="contact-text">info@corvanebuild.com</span>
          <svg class="contact-icon" viewBox="0 0 14 16" aria-hidden="true"><rect x="1" y="4" width="12" height="9" rx="1"/><path d="M1.5 4.5 7 9l5.5-4.5" fill="none" stroke="#fff" stroke-width="1.2"/></svg>
        </li>
        <li class="contact-item">
          <span class="contact-text">www.corvanebuild.com</span>
          <svg class="contact-icon" viewBox="0 0 14 16" aria-hidden="true"><circle cx="7" cy="8" r="6"/><path d="M1 8h12M7 2c-2.2 2.6-2.2 9.4 0 12M7 2c2.2 2.6 2.2 9.4 0 12" fill="none" stroke="#fff" stroke-width="1"/></svg>
        </li>
      </ul>
    </header>

    <section class="letter-meta">
      <p class="meta-date">Date:-</p>
      <p class="meta-subject">Subject:-</p>
    </section>

    <div class="watermark-block" aria-hidden="true"></div>

    <svg class="footer-band" viewBox="0 0 686 15" aria-hidden="true">
      <polygon points="0,0 312,0 350,15 0,15"/>
      <polygon points="336,0 686,0 686,15 374,15"/>
    </svg>
  </main>
</body>
</html>
```